R & T Summit Construction Business Card ideas

We want a business card to represents our company in a way that looks professional but is also a business card that is unique!

Industry/Entity Type

Construction Company

Contact Information for Business Card

open to all design ideas, just want to be able to see different options to choose from in either color or grayscale.

Requirements
Must have
• Our names and phone numbers
• Nolan Pritchett 512-804-2271
• Curtis Hale 512-693-1804
• Business logo

```html
<!DOCTYPE html>
<html lang="en">
<head>
<meta charset="utf-8">
<title>R &amp; T Summit Construction – Business Card</title>
<link href="https://fonts.googleapis.com/css2?family=Questrial&family=Roboto+Condensed:wght@700&display=swap" rel="stylesheet">
<style>
  :root {
    --page: #ecebe8;
    --card-light: #ffffff;
    --card-dark: #0b0b0b;
    --ink: #151515;
    --ink-soft: #6e6e6e;
    --rule: #cfcfcf;
    --paper-white: #f7f7f7;
  }
  * { margin: 0; padding: 0; box-sizing: border-box; }
  html, body {
    width: 1200px; height: 1023px; overflow: hidden;
    background: var(--page);
    font-family: "Questrial", sans-serif;
  }
  .card {
    position: absolute;
    width: 560px; height: 320px;
    border-radius: 4px;
    box-shadow: 0 10px 30px rgba(0,0,0,0.18);
  }
  .card--front {
    left: 80px; top: 110px;
    background: var(--card-light);
    display: flex; align-items: center;
  }
  .card--back {
    left: 560px; top: 590px;
    background: var(--card-dark);
    display: flex; align-items: center; justify-content: center;
  }
  .brand {
    display: flex; flex-direction: column; align-items: flex-start;
  }
  .brand__name {
    font-family: "Questrial", sans-serif;
    font-size: 27px; line-height: 1.1;
    color: var(--ink);
    max-width: 220px;
    padding-bottom: 8px;
    border-bottom: 1.5px solid var(--ink);
  }
  .card--back .brand__name {
    color: var(--paper-white);
    border-bottom-color: var(--paper-white);
    font-size: 32px; max-width: 280px;
  }
  .front__logo {
    width: 300px; height: 100%;
    display: flex; align-items: center; justify-content: center;
  }
  .front__divider {
    width: 1px; height: 100%;
    background: var(--rule);
  }
  .front__contact {
    flex: 1; padding-left: 34px;
    color: var(--ink-soft);
  }
  .person__name {
    font-family: "Roboto Condensed", sans-serif;
    font-weight: 700; font-size: 19px;
    color: var(--ink); letter-spacing: 0.5px;
  }
  .person__role { font-size: 14px; margin-top: 2px; }
  .contact-list { list-style: none; margin-top: 18px; font-size: 13.5px; }
  .contact-list li { display: flex; align-items: center; gap: 8px; margin-bottom: 3px; }
  .contact-list svg { width: 12px; height: 12px; fill: var(--ink); flex: none; }
  .address { margin-top: 22px; font-size: 14px; line-height: 1.35; }
</style>
</head>
<body>
  <section class="card card--front">
    <div class="front__logo">
      <div class="brand"><span class="brand__name">R &amp; T Summit Construction</span></div>
    </div>
    <div class="front__divider"></div>
    <div class="front__contact">
      <p class="person__name">NOLAN PRITCHETT</p>
      <p class="person__role">Managing Director</p>
      <ul class="contact-list">
        <li><svg viewBox="0 0 12 12"><path d="M2.5 0.5l2 2.4-1.1 1.3c.8 1.7 2 2.9 3.6 3.7l1.3-1.1 2.4 2-1 2.2C5 10.8 1.2 7 0.3 1.5z"/></svg>512-804-2271</li>
        <li><svg viewBox="0 0 12 12"><path d="M0 2h12v8H0z M0.8 2.6L6 6.6l5.2-4" fill="none" stroke="#151515" stroke-width="1.2"/></svg>info@rtsummit.com</li>
        <li><svg viewBox="0 0 12 12"><circle cx="6" cy="6" r="5.5"/><path d="M0.5 6h11M6 0.5v11M2 3h8M2 9h8" stroke="#fff" stroke-width="0.8" fill="none"/></svg>www.rtsummit.com</li>
      </ul>
      <p class="address">Here your company<br>or home address</p>
    </div>
  </section>

  <section class="card card--back">
    <div class="brand"><span class="brand__name">R &amp; T Summit Construction</span></div>
  </section>
</body>
</html>
```